Clothing range for the petite modern mature woman needs a card design

We need a business card design for a new Sydney based company called plum twist. We provide clothing to the modern mature woman who finds it difficult to source clothes that do not make them look frumpy or do not fit. We have an idea we would like an apple with the peel unravelling and possibly the silhouette of a woman's body coming out of the peel. The plum twist represents the womans body shape and dressing it.

Target Market(s)

modern mature aged woman

Industry/Entity Type

Clothing

Contact Information for Business Card

abn: 41027395816
will provide email at a later date
a spiel re clothes for modern woman???

Font styles to use
Serif
Sans Serif

Requirements
Must have
• will need name - ABN -will need email address but still working on that (TBA)
Nice to have
• picture of an apple with its peel coming off and possibly the silhouette of a woman coming out. the issue a lot of women in the over 50 range have is that the clothing is very dated or makes the woman frumpy. we are providing clothes for the woman who has difficulty in finding fashionable clothes in their size.
Should not have
• don't want childlike

```html
<!DOCTYPE html>
<html lang="en">
<head>
<meta charset="utf-8">
<title>Plum Twist – Business Card</title>
<link rel="stylesheet" href="https://fonts.googleapis.com/css2?family=Arimo:wght@400&display=swap">
<style>
  :root {
    --backdrop: #ececec;
    --card-white: #ffffff;
    --brand-green: #86c226;
    --brand-grey: #7d8a72;
    --text-white: #ffffff;
  }
  * { margin: 0; padding: 0; box-sizing: border-box; }
  html, body {
    width: 1200px;
    height: 999px;
    overflow: hidden;
    background: var(--backdrop);
    font-family: "Arimo", Arial, sans-serif;
  }
  .canvas { position: relative; width: 1200px; height: 999px; }

  /* Front of card */
  .card-front {
    position: absolute;
    left: 65px; top: 170px;
    width: 398px; height: 658px;
    background: var(--card-white);
  }
  .brand-mark {
    position: absolute;
    left: 159px; top: 230px;
    width: 80px; height: 80px;
  }
  .brand-name {
    position: absolute;
    left: 0; right: 0; top: 424px;
    text-align: center;
    font-size: 40px;
    line-height: 36px;
    font-weight: 400;
    letter-spacing: 3px;
    color: var(--brand-grey);
    white-space: nowrap;
  }
  .brand-tagline {
    position: absolute;
    left: 0; right: 0; top: 459px;
    text-align: center;
    font-size: 17px;
    line-height: 18px;
    color: var(--brand-grey);
    white-space: nowrap;
  }

  /* Back of card */
  .card-back {
    position: absolute;
    left: 512px; top: 311px;
    width: 625px; height: 376px;
    background: var(--brand-green);
  }
  .name-bar {
    position: absolute;
    left: 0;
    width: 276px; height: 33px;
    background: var(--card-white);
    color: var(--brand-green);
    font-size: 22px;
    line-height: 33px;
    text-align: right;
    padding-right: 45px;
  }
  .name-bar--first { top: 150px; }
  .name-bar--second { top: 193px; }
  .contact {
    position: absolute;
    left: 312px;
    font-size: 16px;
    color: var(--text-white);
  }
  .contact--phone-first { top: 159px; }
  .contact--phone-second { top: 203px; }
  .contact--email { top: 242px; }
  .abn {
    position: absolute;
    right: 14px; bottom: 10px;
    font-size: 13px;
    color: var(--text-white);
  }
</style>
</head>
<body>
  <main class="canvas">
    <section class="card-front">
      <svg class="brand-mark" viewBox="0 0 80 80" role="img" aria-label="Brand mark placeholder">
        <circle cx="40" cy="40" r="40" fill="#86c226"/>
      </svg>
      <div class="brand-name">PLUM TWIST</div>
      <div class="brand-tagline">weekend collection for petite women</div>
    </section>

    <section class="card-back">
      <div class="name-bar name-bar--first">Dana Morrow</div>
      <div class="name-bar name-bar--second">Helen Carver</div>
      <div class="contact contact--phone-first">0400 555 318</div>
      <div class="contact contact--phone-second">0400 555 742</div>
      <div class="contact contact--email">plumtwistpetite@example.com</div>
      <div class="abn">abn: 41027395816</div>
    </section>
  </main>
</body>
</html>
```